Kelta Assembly. "Powering Enterprise Renewal" Website

I have established a new company based in Sydney Australia that exists to support large service companies to transform their businesses. I offer a bespoke alternative to the large consulting firms like RJ, Hartwell, TDRW and Brannock. My intention over time is to grow this business with more consulting partners and practitioners and expand into ASIA PAC, Europe and the US.

I would like to create a mobile responsive website that has a similar look and feel to RJ, see URL below plus URLs for Brannock, Hartwell and TDRW.

http://www.rj-example.com/
https://home.tdrw-example.com/au/en/home.html
http://www.brannock-example.com/

I am on a limited budget however so do not require a whole lot of fancy features. Key priorities;

- Responsive to all device types. PC, Tablet, Mobile
- A horizontal scrolling set of hero images that link to particular story or subject like RJ-example.com. 3 only required
- Only limited content is required and most would be static apart from hero scrolling images/topics at top of page
- I would need the ability to be able to remove, replace, update the hero slides every 3-4 months
- Key priority is to present a level of professionalism and look and feel on par with RJ, Hartwell, Brannock and Co, for people to know what I do and how to contact me.
- Link site to my connect up Profile
- My logo is attached and contact details
- I have purchased the domain name www.keltaassembly-example.com.au through sure names

Industry/Entity Type

Management Consulting

Coding

Coded - Design and coding required

Number of Pages Required

1 page

Requirements
Must have
• Mobile responsive to be viewed on any device, simple clean design, easy to find contact details, 3 scrolling articles like RJ-example.com that link to a PDF article. Align colours and theming to Logo on white background attached. Align fonts, look and feel etc to Log design attached

```html
<!DOCTYPE html>
<html lang="en">
<head>
<meta charset="utf-8">
<title>Kelta Assembly — Powering Enterprise Renewal</title>
<link rel="stylesheet" href="https://fonts.googleapis.com/css2?family=PT+Sans:wght@400;700&family=PT+Sans+Narrow:wght@400;700&display=swap">
<style>
:root{
  --accent:#3fc8ef;
  --accent-soft:#a9e3f4;
  --ink:#222;
  --text:#555;
  --rule:#cfcfcf;
  --panel:#f3f3f3;
  --panel-alt:#ececec;
  --sidebar:#ebebeb;
  --dark:#333;
  --field:#666;
  --footer:#666;
  --white:#fff;
  --sq1:#3c5a99;
  --sq2:#5b9bd5;
  --sq3:#1f7bb5;
  --sq4:#d9443a;
}
*{box-sizing:border-box;margin:0;padding:0}
html,body{width:1200px;height:2228px;overflow:hidden}
body{position:relative;background:var(--white);font-family:"PT Sans",Arial,sans-serif;color:var(--text)}
a{color:inherit;text-decoration:none}

/* header */
.site-header{position:absolute;left:0;top:0;width:1200px;height:97px;border-bottom:3px solid var(--accent)}
.brand{position:absolute;left:120px;top:28px;display:flex;align-items:center;gap:10px;font-family:"PT Sans",sans-serif;font-size:20px;letter-spacing:2px;text-transform:uppercase;color:var(--dark)}
.brand-dot{width:12px;height:12px;border-radius:50%;background:var(--accent)}
.util-nav{position:absolute;right:120px;top:14px;font-family:"PT Sans Narrow",sans-serif;font-size:10px;color:#666;letter-spacing:.3px}
.util-nav span{margin:0 6px}
.main-nav{position:absolute;left:493px;top:40px;width:587px;height:54px;border-top:1px solid var(--rule)}
.main-nav a{position:absolute;top:20px;font-family:"PT Sans Narrow",sans-serif;font-size:14px;color:#555}
.main-nav a.active{color:#333}
.main-nav .active-bar{position:absolute;left:0;top:-3px;width:32px;height:3px;background:var(--accent)}
.search-btn{position:absolute;right:0;top:2px;width:54px;height:52px;background:#ececec;display:flex;align-items:center;justify-content:center}

/* hero */
.hero{position:absolute;left:0;top:97px;width:1200px;height:595px;background:linear-gradient(100deg,#2d3340 0%,#3b3a3a 35%,#4b4540 60%,#2f2b28 100%)}
.hero-bar{position:absolute;left:0;top:692px;width:1200px;height:4px;background:var(--accent)}
.hero-card{position:absolute;left:120px;top:190px;width:400px;height:502px}
.hero-card .card-shape{position:absolute;left:0;top:0}
.hero-title{position:absolute;left:30px;top:98px;width:330px;font-family:"PT Sans Narrow",sans-serif;font-weight:700;font-size:30px;line-height:38px;color:var(--ink)}
.hero-rule{position:absolute;left:30px;top:196px;width:336px;height:1px;background:var(--rule)}
.hero-text{position:absolute;left:30px;top:234px;width:325px;font-size:12.5px;line-height:20.5px;color:#666}
.btn{position:absolute;top:377px;height:39px;display:flex;align-items:center;justify-content:center;font-family:"PT Sans Narrow",sans-serif;font-size:13px}
.btn-dark{left:30px;width:103px;background:var(--dark);color:var(--white)}
.btn-accent{left:176px;width:103px;background:var(--accent);color:var(--white)}
.btn-or{position:absolute;left:150px;top:389px;font-size:11px;color:#777}
.slider-arrows{position:absolute;left:30px;top:439px}

/* main */
.sidebar-bg{position:absolute;left:744px;top:696px;width:336px;height:1210px;background:var(--sidebar)}
.section-title{position:absolute;font-family:"PT Sans Narrow",sans-serif;font-weight:700;font-size:21px;color:var(--ink)}
.rule{position:absolute;height:1px;background:#bbb}
.article{position:absolute;left:120px;width:575px;height:119px;background:var(--panel)}
.article.alt{background:var(--panel-alt)}
.article .thumb{position:absolute;left:17px;top:17px;width:123px;height:82px}
.article h3{position:absolute;left:158px;top:12px;font-family:"PT Sans Narrow",sans-serif;font-weight:400;font-size:18px;color:var(--ink)}
.article .meta{position:absolute;left:158px;top:38px;font-size:10px;color:#666}
.article .meta b{font-weight:400;color:#333}
.article p{position:absolute;left:158px;top:57px;width:398px;font-size:9px;line-height:16px;color:#666}
.article p b{font-weight:400;color:#222}

.event{position:absolute;left:120px;width:276px;height:57px}
.event .date{position:absolute;left:0;top:0;width:57px;height:57px;background:#555;color:var(--white);text-align:center}
.event .date .day{display:block;height:38px;line-height:38px;font-family:"PT Sans Narrow",sans-serif;font-weight:700;font-size:21px}
.event .date .mon{display:block;height:19px;line-height:19px;background:#333;font-size:10px}
.event .title{position:absolute;left:68px;top:6px;width:210px;font-family:"PT Sans Narrow",sans-serif;font-size:16.5px;line-height:22px;color:#333}
.map{position:absolute;left:420px;top:1428px;width:275px;height:143px}

.profile{position:absolute;left:120px;top:1633px;width:575px;height:223px;background:var(--panel-alt)}
.profile .photo{position:absolute;left:24px;top:24px;width:101px;height:103px;background:linear-gradient(180deg,#e9e9e9,#bdbdbd 60%,#3a3a3a)}
.profile .find{position:absolute;left:24px;top:146px;font-size:8px;line-height:11px;color:#333}
.profile .socials{position:absolute;left:24px;top:172px;display:flex;gap:5px}
.profile .socials span{width:21px;height:21px}
.profile .name{position:absolute;left:155px;top:26px;font-family:"PT Sans Narrow",sans-serif;font-weight:700;font-size:16px;color:var(--ink)}
.profile .role{font-family:"PT Sans",sans-serif;font-weight:400;font-size:10px;margin-left:12px;color:#333}
.profile .bio{position:absolute;left:155px;top:54px;width:395px;font-size:9.5px;line-height:13px;color:#444}
.profile ul{position:absolute;left:155px;top:112px;width:395px;list-style:none;font-size:9.5px;line-height:13px;color:#444}
.profile li{position:relative;padding-left:16px;margin-bottom:6px}
.profile li::before{content:"";position:absolute;left:0;top:3px;width:7px;height:7px;background:#222}
.profile .more{position:absolute;left:155px;top:186px;font-size:11px;color:#555}
.profile .more b{font-weight:400;color:#222}

.widget{position:absolute;left:759px;width:304px;background:var(--white);border:1px solid var(--accent-soft)}
.widget h4{position:absolute;left:25px;top:28px;font-family:"PT Sans Narrow",sans-serif;font-weight:700;font-size:16px;color:var(--ink)}
.widget .wrule{position:absolute;left:25px;right:22px;top:60px;height:1px;background:#bbb}
.social-row{position:absolute;left:25px;top:86px;display:flex;gap:4px}
.social-row span{width:32px;height:32px}
.contact-intro{position:absolute;left:25px;top:73px;font-size:10px;line-height:19px;color:#555}
.contact-intro b{font-weight:400;color:#222}
.field{position:absolute;left:25px;width:255px;background:var(--field);color:var(--white);font-size:10px;padding:10px 16px}
.send{position:absolute;left:25px;top:260px;width:107px;height:39px;background:var(--field);color:var(--white);font-size:12px;display:flex;align-items:center;justify-content:center;font-family:"PT Sans Narrow",sans-serif}
.see-all{position:absolute;right:24px;top:31px;font-size:9.5px;color:#333}
.popular{position:absolute;left:25px;width:257px}
.popular .ptitle{font-family:"PT Sans Narrow",sans-serif;font-size:16px;line-height:21px;color:#444}
.popular .tags{margin-top:10px;font-size:10px;color:#333}
.popular .tags span{color:#666}
.popular .tags em{font-style:normal;margin-left:22px;color:#555}
.popular-rule{position:absolute;left:25px;width:257px;height:1px;background:#ddd}

/* footer */
.site-footer{position:absolute;left:0;top:1906px;width:1200px;height:322px;background:var(--footer);color:var(--white)}
.footer-brand{position:absolute;left:141px;top:118px;display:flex;align-items:center;gap:10px;font-size:20px;letter-spacing:2px;text-transform:uppercase}
.footer-brand .brand-dot{background:var(--white)}
.footer-col{position:absolute;top:61px}
.footer-col h5{font-family:"PT Sans Narrow",sans-serif;font-weight:700;font-size:15.5px;margin-bottom:14px}
.footer-col a{display:block;font-family:"PT Sans Narrow",sans-serif;font-size:12.5px;line-height:14px;margin-bottom:15px}
.qc-row{position:absolute;left:860px;display:flex;align-items:flex-start;gap:14px;font-family:"PT Sans Narrow",sans-serif;font-size:12.5px}
.qc-row svg{flex:none}
.footer-rule{position:absolute;left:120px;top:261px;width:238px;height:1px;background:#888}
.legal{position:absolute;left:122px;top:285px;font-size:8px}
.legal span{margin:0 7px}
</style>
</head>
<body>

<header class="site-header">
  <a class="brand" href="#"><span class="brand-dot"></span>Kelta Assembly</a>
  <nav class="util-nav">CLIENT PORTAL<span>|</span>NEWSROOM<span>|</span>CONTACT<span>|</span>LANGUAGE</nav>
  <nav class="main-nav">
    <span class="active-bar"></span>
    <a class="active" href="#" style="left:0">HOME</a>
    <a href="#" style="left:65px">INDUSTRIES</a>
    <a href="#" style="left:160px">SERVICES</a>
    <a href="#" style="left:240px">CAREERS</a>
    <a href="#" style="left:319px">EVENTS</a>
    <a href="#" style="left:392px">LOCATIONS</a>
    <a href="#" style="left:483px">ABOUT</a>
    <span class="search-btn">
      <svg width="18" height="18" viewBox="0 0 18 18"><circle cx="7.5" cy="7.5" r="5.5" fill="none" stroke="#555" stroke-width="2"/><line x1="11.5" y1="11.5" x2="16" y2="16" stroke="#555" stroke-width="2.2"/></svg>
    </span>
  </nav>
</header>

<section class="hero" role="img" aria-label="Photo of a consultant reviewing documents at a desk in an office"></section>
<div class="hero-bar"></div>
<div class="hero-card">
  <svg class="card-shape" width="400" height="502" viewBox="0 0 400 502"><polygon points="0,62 400,0 400,502 0,502" fill="#fff"/></svg>
  <h1 class="hero-title">LOREM IPSUM DOLOR SIT AMET, CONSECTETUR</h1>
  <div class="hero-rule"></div>
  <p class="hero-text">sed do eiusmod tempor incididunt ut labore et dolore magna aliqua. Ut enim ad minim veniam, quis nostrud exercitation ulla&shy;mco laboris nisi ut aliquip ex ea commodo consequat. Duis aute irure dolor in reprehenderit in voluptate velit esse cillum dolore eu fugiat nulla pariatur.</p>
  <a class="btn btn-dark" href="#">LEARN MORE</a>
  <span class="btn-or">or</span>
  <a class="btn btn-accent" href="#">CONTACT US</a>
  <svg class="slider-arrows" width="56" height="26" viewBox="0 0 56 26">
    <circle cx="13" cy="13" r="11.5" fill="none" stroke="#333" stroke-width="1.3"/>
    <polyline points="15,8 10,13 15,18" fill="none" stroke="#333" stroke-width="1.4"/>
    <circle cx="40" cy="13" r="11.5" fill="none" stroke="#333" stroke-width="1.3"/>
    <polyline points="38,8 43,13 38,18" fill="none" stroke="#333" stroke-width="1.4"/>
  </svg>
</div>

<div class="sidebar-bg"></div>

<h2 class="section-title" style="left:120px;top:745px">LATEST ARTICLES</h2>
<div class="rule" style="left:120px;top:792px;width:575px"></div>

<article class="article" style="top:817px">
  <div class="thumb" role="img" aria-label="Photo of a laptop and a red coffee cup on a wooden desk" style="background:linear-gradient(135deg,#4a4039,#6b5b4d 55%,#b33a22 75%,#5a4a3d)"></div>
  <h3>Sed do eiusmod tempor incididunt ut labore et dolore</h3>
  <div class="meta">by <b>Teo Marsh</b> on Jun 15, 2016</div>
  <p>laboris nisi ut aliquip ex ea commodo consequat. Duis aute irure dolor in reprehenderit in voluptate velit esse cillum dolore eu fugiat nulla pariatur. Excepteur sint occaecat cupidatat non proident, sunt in culpa qui officia deserunt mollit anim id est laborum <b>Read More</b></p>
</article>
<article class="article alt" style="top:944px">
  <div class="thumb" role="img" aria-label="Photo of a person working at a computer desk" style="background:linear-gradient(135deg,#5b4b6a,#b9a9c8 50%,#e8e1ea)"></div>
  <h3>Sed do eiusmod tempor incididunt ut labore et dolore</h3>
  <div class="meta">by <b>Teo Marsh</b> on Jun 15, 2016</div>
  <p>laboris nisi ut aliquip ex ea commodo consequat. Duis aute irure dolor in reprehenderit in voluptate velit esse cillum dolore eu fugiat nulla pariatur. Excepteur sint occaecat cupidatat non proident, sunt in culpa qui officia deserunt mollit anim id est laborum <b>Read More</b></p>
</article>
<article class="article" style="top:1072px">
  <div class="thumb" role="img" aria-label="Photo of a laptop and a red coffee cup on a wooden desk" style="background:linear-gradient(135deg,#4a4039,#6b5b4d 55%,#b33a22 75%,#5a4a3d)"></div>
  <h3>Sed do eiusmod tempor incididunt ut labore et dolore</h3>
  <div class="meta">by <b>Teo Marsh</b> on Jun 15, 2016</div>
  <p>laboris nisi ut aliquip ex ea commodo consequat. Duis aute irure dolor in reprehenderit in voluptate velit esse cillum dolore eu fugiat nulla pariatur. Excepteur sint occaecat cupidatat non proident, sunt in culpa qui officia deserunt mollit anim id est laborum <b>Read More</b></p>
</article>
<article class="article alt" style="top:1200px">
  <div class="thumb" role="img" aria-label="Photo of hands signing paperwork on a desk" style="background:linear-gradient(135deg,#1e1e1e,#3a3634 50%,#d9d7d3 80%,#2a2a2a)"></div>
  <h3>Sed do eiusmod tempor incididunt ut labore et dolore</h3>
  <div class="meta">by <b>Teo Marsh</b> on Jun 15, 2016</div>
  <p>laboris nisi ut aliquip ex ea commodo consequat. Duis aute irure dolor in reprehenderit in voluptate velit esse cillum dolore eu fugiat nulla pariatur. Excepteur sint occaecat cupidatat non proident, sunt in culpa qui officia deserunt mollit anim id est laborum <b>Read More</b></p>
</article>

<h2 class="section-title" style="left:120px;top:1382px;font-size:17px">UPCOMING EVENTS</h2>
<div class="rule" style="left:120px;top:1418px;width:276px"></div>
<h2 class="section-title" style="left:420px;top:1382px;font-size:17px">FIND BY LOCATION</h2>
<div class="rule" style="left:420px;top:1418px;width:275px"></div>

<div class="event" style="top:1440px">
  <div class="date"><span class="day">18</span><span class="mon">JUN</span></div>
  <div class="title">Lorem ipsum dolor sit amet, con-<br>sectetur adipiscing</div>
</div>
<div class="event" style="top:1512px">
  <div class="date"><span class="day">22</span><span class="mon">JUN</span></div>
  <div class="title">Lorem ipsum dolor sit amet, con-<br>sectetur adipiscing</div>
</div>
<div class="map" role="img" aria-label="Map of North America with office location markers" style="background:linear-gradient(120deg,#e6e6e6,#b5b5b5 50%,#e6e6e6)"></div>

<section class="profile">
  <div class="photo" role="img" aria-label="Portrait photo of the founder"></div>
  <div class="find">You can find Rory Vane<br>on social platforms also:</div>
  <div class="socials" aria-label="Social profiles">
    <span style="background:var(--sq1)"></span><span style="background:var(--sq3)"></span><span style="background:var(--sq2)"></span><span style="background:var(--sq4)"></span>
  </div>
  <div class="name">RORY VANE<span class="role">Founder Kelta Assembly</span></div>
  <p class="bio">Rory is originally from New Zealand and has worked across sales, operations, strategy and program delivery in NZ, the United Kingdom and Australia.<br>Rory has;</p>
  <ul>
    <li>Experience in multiple industries. Retail, Telco and Investment and Retail banking</li>
    <li>Over 15+ years experience working in financial services</li>
    <li>Successfully led the turn around of a number of businesses including the<br>Harbourline Group Merchants / Payments Transformation and "Bridge".</li>
  </ul>
  <div class="more">Find more about <b>Rory</b></div>
</section>

<aside class="widget" style="top:719px;height:160px">
  <h4>FIND US ON</h4>
  <div class="wrule"></div>
  <div class="social-row" aria-label="Social profiles">
    <span style="background:var(--sq1)"></span><span style="background:var(--sq2)"></span><span style="background:var(--sq3)"></span><span style="background:var(--sq4)"></span>
  </div>
</aside>

<aside class="widget" style="top:912px;height:338px">
  <h4>CONTACT US</h4>
  <div class="wrule"></div>
  <p class="contact-intro">Any question or query regarding our work, our services?<br>Please feel free to <b>Contact Us</b></p>
  <div class="field" style="top:122px;height:39px">Email Address</div>
  <div class="field" style="top:169px;height:81px">Your message here...</div>
  <a class="send" href="#">SEND</a>
</aside>

<aside class="widget" style="top:1282px;height:430px">
  <h4>MOST POPULAR</h4>
  <a class="see-all" href="#">See All</a>
  <div class="wrule"></div>
  <div class="popular" style="top:82px">
    <div class="ptitle">Family Business split rate highest ever in South Carolina estate</div>
    <div class="tags">Tags: <span>Family, Business</span><em>159 Views</em></div>
  </div>
  <div class="popular-rule" style="top:169px"></div>
  <div class="popular" style="top:193px">
    <div class="ptitle">Family Business split rate highest ever in South Carolina estate</div>
    <div class="tags">Tags: <span>Family, Business</span><em>159 Views</em></div>
  </div>
  <div class="popular-rule" style="top:281px"></div>
  <div class="popular" style="top:305px">
    <div class="ptitle">Family Business split rate highest ever in South Carolina estate</div>
    <div class="tags">Tags: <span>Family, Business</span><em>159 Views</em></div>
  </div>
</aside>

<footer class="site-footer">
  <div class="footer-brand"><span class="brand-dot"></span>Kelta Assembly</div>
  <div class="footer-col" style="left:428px">
    <h5>About</h5>
    <a href="#">Our Values</a><a href="#">Market Approach</a><a href="#">Our Team</a><a href="#">Client Portal</a><a href="#">Regional Affiliation</a><a href="#">Working Fields</a>
  </div>
  <div class="footer-col" style="left:576px">
    <h5>Services</h5>
    <a href="#">Our Values</a><a href="#">Market Approach</a><a href="#">Our Team</a><a href="#">Client Portal</a><a href="#">Regional Affiliation</a><a href="#">Working Fields</a>
  </div>
  <div class="footer-col" style="left:723px">
    <h5>Careers</h5>
    <a href="#">Our Values</a><a href="#">Market Approach</a><a href="#">Our Team</a><a href="#">Client Portal</a>
  </div>
  <div class="footer-col" style="left:860px">
    <h5>Quick Contact</h5>
  </div>
  <div class="qc-row" style="top:97px">
    <svg width="16" height="16" viewBox="0 0 16 16"><circle cx="8" cy="4.5" r="3.8" fill="#fff"/><path d="M1 16c0-4.5 3-7 7-7s7 2.5 7 7z" fill="#fff"/></svg>
    <div><span style="font-size:15px">Rory Vane</span><br>Director</div>
  </div>
  <div class="qc-row" style="top:151px">
    <svg width="16" height="16" viewBox="0 0 16 16"><path d="M3 1l3 3-1.6 2.2c.9 2 2.4 3.5 4.4 4.4L11 9l3 3-2 3C6 14.5 1.5 10 1 3z" fill="#fff"/></svg>
    <div>+61400555019</div>
  </div>
  <div class="qc-row" style="top:190px">
    <svg width="16" height="14" viewBox="0 0 16 14"><rect x="0" y="1" width="16" height="12" fill="#fff"/><polyline points="0,1.5 8,8 16,1.5" fill="none" stroke="#666" stroke-width="1.4"/></svg>
    <div>rory@keltaassembly-example.com.au</div>
  </div>
  <div class="qc-row" style="top:229px">
    <svg width="16" height="16" viewBox="0 0 16 16" fill="none" stroke="#fff" stroke-width="1.4"><circle cx="8" cy="8" r="7"/><ellipse cx="8" cy="8" rx="3" ry="7"/><line x1="1" y1="8" x2="15" y2="8"/></svg>
    <div>www.keltaassembly-example.com.au</div>
  </div>
  <div class="footer-rule"></div>
  <div class="legal">Terms &amp; Conditions<span>|</span>Privacy Policy</div>
</footer>

</body>
</html>
```